Orbin Vale Systems

Our company is about IT hardwares and IT solutions. IT hardware such as PC, RAMS, storage and servers. IT solutions such as project management, BA. We are also selling new technology too.

Target Market(s)

Consumer, Small to Medium Business, Corporate

Requirements
Must have
• The business card must have the following:
• Name:
• Title:
• Contact Number:
• Email address:
• Website:
• Color: Must match the logo color upgrade

```html
<!DOCTYPE html>
<html lang="en">
<head>
<meta charset="utf-8">
<title>Orbin Vale Systems – Business Card</title>
<link rel="stylesheet" href="https://fonts.googleapis.com/css2?family=Montserrat:wght@400;500;700&display=swap">
<style>
  :root {
    --backdrop: #e6e3df;
    --card-dark: #2b2b2c;
    --card-light: #ffffff;
    --accent: #e08a1e;
    --ink: #333333;
    --ink-soft: #555555;
    --rule: #c9c9c9;
    --metal: #d9d9d9;
  }
  * { box-sizing: border-box; margin: 0; padding: 0; }
  html, body {
    width: 1200px; height: 854px; overflow: hidden;
    background: var(--backdrop);
    font-family: "Montserrat", sans-serif;
  }
  .sheet {
    width: 1200px; height: 854px;
    display: flex; align-items: center; justify-content: center; gap: 40px;
  }
  .card {
    width: 520px; height: 297px; position: relative; overflow: hidden;
    box-shadow: 0 10px 26px rgba(0,0,0,.18);
  }
  .card--front {
    background: var(--card-dark);
    border-bottom: 6px solid var(--accent);
    display: flex; align-items: center; justify-content: center;
  }
  .card--back { background: var(--card-light); }
  .card--back .band {
    position: absolute; left: 0; right: 0; bottom: 0; height: 12px;
    background: var(--accent);
  }
  .brand {
    display: flex; align-items: center; gap: 12px;
  }
  .brand__dot {
    width: 18px; height: 18px; border-radius: 50%; background: var(--accent); flex: none;
  }
  .brand__name {
    font-weight: 700; letter-spacing: 1px; line-height: 1.05; text-transform: uppercase;
  }
  .card--front .brand__name { color: var(--metal); font-size: 34px; }
  .card--back .brand__name { color: var(--ink); font-size: 22px; }
  .card--back .brand {
    position: absolute; left: 34px; top: 50%; transform: translateY(-50%);
    width: 210px;
  }
  .divider {
    position: absolute; left: 258px; top: 58px; bottom: 58px; width: 1px; background: var(--rule);
  }
  .contact {
    position: absolute; left: 282px; top: 62px; color: var(--ink-soft);
    font-size: 12.5px; line-height: 1.5;
  }
  .contact__name {
    color: var(--accent); font-weight: 700; font-size: 17px; text-transform: uppercase; line-height: 1.1;
  }
  .contact__title { color: var(--ink); font-weight: 500; margin-bottom: 10px; }
  .contact__address { margin-bottom: 6px; }
  .contact__row { display: flex; align-items: center; gap: 8px; }
  .contact__row svg { width: 12px; height: 12px; flex: none; }
</style>
</head>
<body>
<main class="sheet">
  <section class="card card--front">
    <div class="brand">
      <span class="brand__dot"></span>
      <span class="brand__name">Orbin Vale<br>Systems</span>
    </div>
  </section>

  <section class="card card--back">
    <div class="brand">
      <span class="brand__dot"></span>
      <span class="brand__name">Orbin Vale<br>Systems</span>
    </div>
    <div class="divider"></div>
    <div class="contact">
      <p class="contact__name">Daren Holt</p>
      <p class="contact__title">Managing Director</p>
      <p class="contact__address">Kade Street 48<br>9000 Lunmere Vale</p>
      <p class="contact__row">
        <svg viewBox="0 0 12 12" aria-hidden="true"><path d="M3 1l2 2.5-1.2 1.3a7 7 0 0 0 3.4 3.4L8.5 7 11 9l-1.2 2C5 11 1 7 1 2.2z" fill="none" stroke="#e08a1e" stroke-width="1"/></svg>
        + 12 555 0142 88
      </p>
      <p class="contact__row">
        <svg viewBox="0 0 12 12" aria-hidden="true"><rect x="1" y="2.5" width="10" height="7" fill="none" stroke="#e08a1e" stroke-width="1"/><path d="M1 2.5l5 4 5-4" fill="none" stroke="#e08a1e" stroke-width="1"/></svg>
        daren@orbinvale.com
      </p>
      <p class="contact__row">
        <svg viewBox="0 0 12 12" aria-hidden="true"><circle cx="6" cy="6" r="5" fill="none" stroke="#e08a1e" stroke-width="1"/><ellipse cx="6" cy="6" rx="2.2" ry="5" fill="none" stroke="#e08a1e" stroke-width="1"/><path d="M1 6h10" stroke="#e08a1e" stroke-width="1"/></svg>
        www.orbinvale.com
      </p>
    </div>
    <div class="band"></div>
  </section>
</main>
</body>
</html>
```